Zentraly Wordpress Website Update

Over the course of the past two years the website has become bloated and slow. It is at Zentraly.net. The refresh does not need to be an exact copy but should have the same elements of a high technology consulting firm specializing is audio video. The company tag line is "AV Experts in Experiential Design".
The intent is to add a section on the front page that has the "latest news" or selected highlights. As an example the company is underwriting a trade event and we want to list that on there. The pages should be a front page, about, contact, services, and blog.
I have included assets that Zentraly already owns as well as the color templates that were recommended. The overall look thought should be brighter which is why the backgrounds are lighter greens. I have provided all of the assets as I realize that my choices might not have been the best ones.
It is very important that this page be Responsive so that it works on mobile.

Target Market(s)

Theme parks, museums, corporate environments, business to business

Industry/Entity Type

Professional Audio Video

Coding

Font styles to use
Sans Serif
Other font styles liked:
• Raleway & Roboto

Requirements
Must have
• Responsive design. Ability to post news and thoughts, a blog
Nice to have
• I would like to have a design that can also have complimentary

```html
<!DOCTYPE html>
<html lang="en">
<head>
<meta charset="utf-8">
<title>Zentraly</title>
<link href="https://fonts.googleapis.com/css2?family=Ubuntu:wght@400;500;700&family=Roboto:wght@400;500&display=swap" rel="stylesheet">
<style>
:root{
  --green:#05675a;
  --green-dark:#034f46;
  --navy:#041d2c;
  --navy-2:#06344a;
  --ink:#111;
  --muted:#777;
  --light:#f4f4f4;
  --white:#fff;
  --black:#000;
}
*{box-sizing:border-box;margin:0;padding:0}
html,body{width:1200px;height:3896px;overflow:hidden}
body{position:relative;background:var(--white);font-family:Roboto,Arial,sans-serif;color:var(--ink)}
a{text-decoration:none}
.abs{position:absolute}
h1,h2,h3,.brand,.btn,.link{font-family:Ubuntu,Arial,sans-serif}

/* header */
.site-header{left:0;top:0;width:1200px;height:92px;background:var(--white)}
.brand{display:flex;align-items:center;gap:10px;color:var(--ink);font-size:30px;font-weight:500;line-height:1}
.brand-dot{width:14px;height:14px;border-radius:50%;background:var(--green);display:block}
.site-header .brand{left:110px;top:29px}
.nav a{position:absolute;top:36px;font-size:15px;color:#222;font-family:Roboto,Arial,sans-serif}
.nav a.active{color:var(--green)}
.btn{display:flex;align-items:center;justify-content:center;border-radius:30px;background:var(--green);color:var(--white);font-weight:500;font-size:15px}
.btn-contact{left:950px;top:22px;width:138px;height:46px}

/* hero */
.hero{left:0;top:92px;width:1200px;height:700px;background:radial-gradient(ellipse at 35% 45%,var(--navy-2),var(--navy) 70%)}
.hero-eyebrow{left:112px;top:176px;font-size:16px;color:#0b8a78}
.hero h1{left:110px;top:198px;color:var(--white);font-size:44px;font-weight:500;line-height:52px}
.hero p{left:112px;top:323px;color:#dfe8ee;font-size:15.5px;line-height:26px;width:420px}
.btn-hero{left:112px;top:401px;width:152px;height:56px}
.hero-photo{left:625px;top:68px;width:460px;height:460px;border-radius:50%;background:radial-gradient(circle at 40% 35%,#5a6b78,#26323c 60%,#1a232b);border:12px solid var(--green)}
.hero-tail{left:620px;top:420px}

/* services */
.section-title{width:1200px;left:0;text-align:center;font-size:34px;font-weight:500}
.card{width:310px;height:360px;top:922px;background:var(--white);box-shadow:0 4px 18px rgba(0,0,0,.08);border-radius:4px;text-align:center;padding:0 24px}
.card .icon{width:88px;height:88px;border-radius:50%;background:#8d9196;margin:32px auto 0;display:flex;align-items:center;justify-content:center}
.card h3{font-size:20px;font-weight:500;margin-top:24px;line-height:26px}
.card p{font-size:14.5px;line-height:26px;color:var(--muted);margin-top:14px}
.link{color:var(--green);font-size:14.5px;font-weight:500}
.card .link{position:absolute;left:0;width:100%;bottom:34px;text-align:center}
.card-featured{background:linear-gradient(160deg,#0a6e69,#0b5d5a 50%,#0e7c72);color:var(--white)}
.card-featured h3{margin-top:46px}
.card-featured p{color:#e3f1ef}
.card-featured .link{color:var(--white)}

/* about */
.about{left:0;top:1373px;width:1200px;height:410px;background:linear-gradient(180deg,#0b6c66,#06574f 55%,#054e47);text-align:center}
.about h2{margin-top:48px;color:var(--white);font-size:35px;font-weight:500}
.about p{width:860px;margin:18px auto 0;color:#e8f3f2;font-size:15px;line-height:26px}
.btn-light{left:524px;top:288px;width:152px;height:56px;background:var(--white);color:var(--green)}

/* news */
.post{background:var(--white);box-shadow:0 4px 18px rgba(0,0,0,.08)}
.post-main{left:111px;top:1937px;width:480px;height:518px}
.post-main .thumb{left:11px;top:10px;width:460px;height:318px;background:linear-gradient(180deg,#0c1c3a,#1f4d8a 60%,#0e2244)}
.post h3{font-size:22px;font-weight:500;line-height:30px}
.meta{font-size:15px;color:var(--muted);display:flex;align-items:center;gap:8px}
.post .excerpt{font-size:14.5px;line-height:26px;color:#222}
.post-side{left:618px;width:470px;height:250px}
.post-side .thumb{left:11px;top:11px;width:224px;height:228px;background:linear-gradient(160deg,#2c4a60,#123046 60%,#0b1f30)}
.post-side .body{left:252px;top:18px;width:205px}

/* contact */
.contact{left:0;top:2533px;width:1200px;height:960px;background:var(--light)}
.contact .lead{left:270px;top:117px;width:660px;text-align:center;color:var(--muted);font-size:15px;line-height:24px}
.form{left:179px;top:210px;width:840px;height:511px;background:var(--white);border-radius:6px}
.field{position:absolute;background:var(--light);border-radius:32px;font-size:12px;color:#555;padding:22px 26px}
.btn-submit{left:348px;top:419px;width:133px;height:55px}

/* footer */
.footer{left:0;top:3420px;width:1200px;height:476px;background:var(--black);color:var(--white)}
.footer .brand{left:112px;top:180px;color:var(--white);font-size:28px}
.social{left:138px;top:242px;display:flex;gap:8px}
.social span{width:28px;height:28px;border-radius:50%;background:var(--white);display:block}
.footer h4{font-family:Ubuntu,sans-serif;font-size:19px;font-weight:500}
.footer ul{list-style:none;font-size:15px;line-height:30px;margin-top:22px}
.footer .row{display:flex;gap:14px;font-size:15px;line-height:24px;margin-bottom:10px}
.footer .row svg{flex:none;margin-top:4px}
.newsletter-input{left:810px;top:225px;width:272px;height:43px;border-radius:22px;background:var(--white);color:#999;font-size:14px;padding:12px 20px}
.newsletter-input .go{position:absolute;right:4px;top:4px;width:35px;height:35px;border-radius:50%;background:var(--green);display:flex;align-items:center;justify-content:center}
.divider{left:110px;top:373px;width:980px;height:1px;background:#333}
.copy{left:0;top:410px;width:1200px;text-align:center;font-size:15px}
</style>
</head>
<body>

<header class="site-header abs">
  <a class="brand abs" href="#"><span class="brand-dot"></span>Zentraly</a>
  <nav class="nav">
    <a class="active" style="left:442px" href="#">Home</a>
    <a style="left:534px" href="#">Services</a>
    <a style="left:643px" href="#">News</a>
    <a style="left:733px" href="#">About Us</a>
    <a style="left:848px" href="#">Blog</a>
  </nav>
  <a class="btn btn-contact abs" href="#">Contact Us</a>
</header>

<section class="hero abs">
  <div class="hero-eyebrow abs">WHO ARE WE?</div>
  <h1 class="abs">AV experts in<br>experiential design</h1>
  <p class="abs">Creating authentic immersive experiences by connecting the dots between people, spaces, and technology.</p>
  <a class="btn btn-hero abs" href="#">Get Started</a>
  <svg class="hero-tail abs" width="120" height="110" viewBox="0 0 120 110"><path d="M20 10 L5 100 L110 70 Z" fill="#05675a"/></svg>
  <div class="hero-photo abs" role="img" aria-label="Consultants reviewing plans on a laptop and tablet in an office"></div>
  <svg class="abs" style="left:0;top:548px" width="1200" height="170" viewBox="0 0 1200 170">
    <path d="M0 58 Q160 120 270 122 L1200 48 L1200 170 L0 170Z" fill="#fff"/>
    <path d="M0 66 Q160 128 270 130 L1200 56" fill="none" stroke="#05675a" stroke-width="8"/>
    <path d="M0 84 Q160 146 270 148 L1200 74" fill="none" stroke="#05675a" stroke-width="8"/>
  </svg>
</section>

<h2 class="section-title abs" style="top:840px">Our Services</h2>

<article class="card abs" style="left:111px">
  <div class="icon"><svg width="46" height="46" viewBox="0 0 46 46" fill="none" stroke="#fff" stroke-width="2"><circle cx="23" cy="14" r="6"/><circle cx="10" cy="20" r="4"/><circle cx="36" cy="20" r="4"/><path d="M8 36 Q23 24 38 36"/></svg></div>
  <h3>Planning &amp; Ideation</h3>
  <p>Our team will partner with you to determine if a concept is valid and that the equipment specified can function as needed to support objectives.</p>
  <a class="link" href="#">Learn More »</a>
</article>
<article class="card card-featured abs" style="left:444px">
  <h3>Content Creation</h3>
  <p>The Zentraly Group is ready to create compelling content for you. The team has written press releases, thought or opinion articles, analysis pieces, white papers, product reviews, application notes, operations manuals, news content and much more.</p>
  <a class="link" href="#">Learn More »</a>
</article>
<article class="card abs" style="left:777px">
  <div class="icon"><svg width="46" height="46" viewBox="0 0 46 46" fill="none" stroke="#fff" stroke-width="2"><rect x="8" y="10" width="16" height="12"/><rect x="22" y="26" width="16" height="10"/><circle cx="34" cy="14" r="5"/><path d="M16 22v8h6"/></svg></div>
  <h3>Design Engineering &amp; Commissioning</h3>
  <p>We will partner with you to provide independent design and engineering services customized</p>
  <a class="link" href="#">Learn More »</a>
</article>

<section class="about abs" role="img" aria-label="Night city skyline with rising light lines">
  <h2>About AV experts in experiential design</h2>
  <p>Zentraly helps create authentic immersive experiences by connecting the dots between people, spaces, and technology. Physical spaces can be permanent, semi-permanent, or entirely temporary. Our mastery in audio, video, lighting, and control, combined with a deep understanding of how people interact with a space, enables Zentraly to create the ultimate connection between humans and technology infrastructure. We blend industry expertise with a resolve for tackling new challenges to elevate the client experience. Every project is unique; not all solutions are the same. We combine tools of strategy, creativity, design, and innovation to deliver a tailored solution that aligns</p>
  <a class="btn btn-light abs" href="#">Learn More</a>
</section>

<h2 class="section-title abs" style="top:1853px">Latest News And Blog</h2>

<article class="post post-main abs">
  <div class="thumb abs" role="img" aria-label="Aerial view of a city at night with glowing data lines"></div>
  <div class="abs" style="left:15px;top:340px;width:450px">
    <h3>007-Commentary</h3>
    <div class="meta" style="margin-top:12px"><svg width="14" height="14" viewBox="0 0 14 14"><rect x="1" y="2" width="12" height="11" fill="none" stroke="#05675a" stroke-width="1.5"/><path d="M1 5h12" stroke="#05675a" stroke-width="1.5"/></svg>April 15, 2021</div>
    <p class="excerpt" style="margin-top:10px">Lorem ipsum dolor sit amet, consectetur adipiscing elit, sed do eiusmod tempor incididunt ut labore et dolore</p>
    <a class="link" href="#">Learn More</a>
  </div>
</article>

<article class="post post-side abs" style="top:1937px">
  <div class="thumb abs" role="img" aria-label="Two engineers reviewing a tablet in a server room"></div>
  <div class="body abs">
    <h3>The Ideation Process is Powerful</h3>
    <div class="meta" style="margin-top:10px"><svg width="14" height="14" viewBox="0 0 14 14"><rect x="1" y="2" width="12" height="11" fill="none" stroke="#05675a" stroke-width="1.5"/><path d="M1 5h12" stroke="#05675a" stroke-width="1.5"/></svg>November 30, 2020</div>
    <p class="excerpt" style="margin-top:6px">Lorem ipsum dolor sit amet, consectetur adipiscing elit, sed do eiusmod tempor</p>
    <a class="link" href="#" style="display:block;margin-top:6px">Learn More</a>
  </div>
</article>

<article class="post post-side abs" style="top:2205px">
  <div class="thumb abs" role="img" aria-label="Two colleagues in a data center pointing at screens"></div>
  <div class="body abs">
    <h3>006-Rise of Skyline</h3>
    <div class="meta" style="margin-top:10px"><svg width="14" height="14" viewBox="0 0 14 14"><rect x="1" y="2" width="12" height="11" fill="none" stroke="#05675a" stroke-width="1.5"/><path d="M1 5h12" stroke="#05675a" stroke-width="1.5"/></svg>April 1, 2021</div>
    <p class="excerpt" style="margin-top:6px">Lorem ipsum dolor sit amet, consectetur adipiscing elit, sed do eiusmod tempor</p>
    <a class="link" href="#" style="display:block;margin-top:6px">Learn More</a>
  </div>
</article>

<section class="contact abs">
  <h2 class="section-title abs" style="top:55px">Contact Us</h2>
  <p class="lead abs">Lorem ipsum dolor sit amet, consectetur adipiscing elit, sed do eiusmod tempor incididunt ut labore et dolore magna aliqua. Quis ipsum suspendisse ultrices gravida.</p>
  <form class="form abs">
    <div class="field" style="left:57px;top:55px;width:353px;height:62px">Name</div>
    <div class="field" style="left:430px;top:55px;width:352px;height:62px">Email</div>
    <div class="field" style="left:57px;top:140px;width:725px;height:62px">Subject</div>
    <div class="field" style="left:57px;top:225px;width:725px;height:155px;border-radius:24px">Message</div>
    <a class="btn btn-submit abs" href="#">Submit</a>
  </form>
</section>

<svg class="abs" style="left:0;top:3360px" width="1200" height="100" viewBox="0 0 1200 100">
  <path d="M0 100 L0 62 L960 12 Q1080 20 1200 82 L1200 100Z" fill="#000"/>
  <path d="M0 54 L960 4 Q1080 12 1200 74" fill="none" stroke="#05675a" stroke-width="8"/>
  <path d="M0 70 L960 20 Q1080 28 1200 90" fill="none" stroke="#fff" stroke-width="4"/>
</svg>

<footer class="footer abs">
  <a class="brand abs" href="#"><span class="brand-dot"></span>Zentraly</a>
  <div class="social abs"><span></span><span></span><span></span><span></span></div>
  <div class="abs" style="left:371px;top:114px">
    <h4>Quick Link</h4>
    <ul><li>Home</li><li>About</li><li>Our Services</li><li>News</li><li>Our Blog</li><li>Contact Us</li></ul>
  </div>
  <div class="abs" style="left:524px;top:116px;width:240px">
    <h4>Contact Us</h4>
    <div style="margin-top:22px">
      <div class="row"><svg width="14" height="14" viewBox="0 0 14 14"><path d="M7 1a4 4 0 0 1 4 4c0 3-4 8-4 8S3 8 3 5a4 4 0 0 1 4-4z" fill="#fff"/></svg><span>2250 Lakeview Court Suite 40 – PMB12 Oak Hollow, FL 30000</span></div>
      <div class="row"><svg width="14" height="14" viewBox="0 0 14 14"><rect x="1" y="3" width="12" height="9" fill="#fff"/><path d="M1 3l6 5 6-5" stroke="#000" fill="none"/></svg><span>info@zentraly.net</span></div>
      <div class="row"><svg width="14" height="14" viewBox="0 0 14 14"><path d="M3 1l3 3-2 2c1 2 2 3 4 4l2-2 3 3-2 2C6 13 1 8 1 3z" fill="#fff"/></svg><span>+1 (555) 014-2730</span></div>
    </div>
  </div>
  <div class="abs" style="left:808px;top:114px;width:290px">
    <h4>Subscribe To Our Newsletter</h4>
    <p style="font-size:15px;line-height:24px;margin-top:22px">Lorem ipsum dolor sit amet, consectetur adipiscing elit, sed do</p>
  </div>
  <div class="newsletter-input abs">Enter Your Email<span class="go"><svg width="16" height="16" viewBox="0 0 16 16"><path d="M1 8l14-6-5 13-2-5z" fill="#fff"/></svg></span></div>
  <div class="divider abs"></div>
  <div class="copy abs">©Copyrights 2022 Zentraly &nbsp;| &nbsp; All Rights Reserved</div>
</footer>

</body>
</html>
```